Business Card Design for high end dental office

Please include attached logo with office name in the font selected for business card design. Emphasis will be on elegance, simplicity with a modern look. We are a high end boutique dental office that focuses on customer service and expertise of our doctors.

The current font chosen for the letters is Garamond, but we are open to suggestions.

The main theme color for the office is cyan and silver.

Target Market(s)

Oral health/esthetics driven adults of the Los Angeles area aged 25 to 80 with above average median household income. Customers range from young professionals such doctors, lawyers, engineers, or entrepreneurs to retired senior citizens.

Industry/Entity Type

Boutique

Colors

Designer to choose colors to be used in the design.

Requirements
Must have
• Business logo and name
Doctor's name and degrees: Elliot Marsh, DDS, MMSc
Doctor's field of work: Smile Solutions/Prosthodontics/Implant Dentistry
Nice to have
• Rounded business card corners.
Background or watermark of logo.
Matte cyan with shiny silver color.
Textured feel.

Files

```html
<!DOCTYPE html>
<html lang="en">
<head>
<meta charset="utf-8">
<title>Silverline Dentistry — Business Card</title>
<link rel="stylesheet" href="https://fonts.googleapis.com/css2?family=EB+Garamond:wght@400;500;600&family=Open+Sans:wght@400;600&display=swap">
<style>
  :root {
    --backdrop: #e9e6e1;
    --card-black: #0d0f10;
    --card-black-soft: #2a2e30;
    --cyan: #6fd3dc;
    --cyan-deep: #4fb2bd;
    --cyan-pale: #a9e4ea;
    --silver: #c9cfd2;
    --silver-dark: #8e979b;
    --white: #f4f7f8;
    --band-text: #1d4a50;
    --back-text: #eaf8fa;
  }
  * { box-sizing: border-box; margin: 0; padding: 0; }
  html, body { width: 1200px; height: 1023px; overflow: hidden; }
  body {
    background: var(--backdrop);
    position: relative;
    font-family: "Open Sans", Arial, sans-serif;
  }
  .card {
    position: absolute;
    left: 190px;
    width: 820px;
    height: 470px;
    border-radius: 28px;
    overflow: hidden;
    box-shadow: 0 10px 28px rgba(0,0,0,0.25);
  }
  /* Front */
  .card-front {
    top: 30px;
    background: linear-gradient(150deg, var(--card-black-soft) 0%, var(--card-black) 45%, #050606 100%);
    color: var(--white);
  }
  .brand-mark {
    position: absolute;
    left: 56px;
    top: 70px;
    display: flex;
    align-items: center;
    gap: 16px;
  }
  .brand-dot {
    width: 46px; height: 46px;
    border-radius: 50%;
    background: var(--cyan);
  }
  .brand-name {
    font-family: "EB Garamond", Garamond, serif;
    font-weight: 500;
    font-size: 38px;
    letter-spacing: 3px;
    text-transform: uppercase;
    color: var(--silver);
    line-height: 1.05;
  }
  .doctor {
    position: absolute;
    left: 58px;
    top: 192px;
    font-family: "EB Garamond", Garamond, serif;
    font-weight: 400;
    color: var(--cyan);
    font-size: 34px;
    letter-spacing: 1.5px;
    font-variant: small-caps;
    white-space: nowrap;
  }
  .doctor .credentials {
    font-family: "Open Sans", Arial, sans-serif;
    font-size: 18px;
    font-variant: normal;
    letter-spacing: 0.5px;
  }
  .contact-list {
    position: absolute;
    left: 58px;
    top: 262px;
    list-style: none;
    font-size: 17px;
    color: var(--white);
  }
  .contact-list li { display: flex; align-items: center; gap: 12px; margin-bottom: 9px; }
  .contact-icon { width: 20px; height: 20px; flex: none; }
  .divider {
    position: absolute;
    left: 560px;
    top: 40px;
    width: 1px;
    height: 300px;
    background: linear-gradient(to bottom, transparent, var(--silver-dark), transparent);
  }
  .office {
    position: absolute;
    right: 48px;
    top: 120px;
    text-align: right;
    font-size: 18px;
    line-height: 1.5;
    font-style: normal;
  }
  .office-name { color: var(--cyan); font-weight: 600; font-size: 19px; }
  .specialty-band {
    position: absolute;
    left: 0; right: 0; bottom: 0;
    height: 64px;
    background: linear-gradient(180deg, var(--cyan-pale), var(--cyan-deep));
    display: flex;
    align-items: center;
    justify-content: center;
    color: var(--band-text);
    font-size: 17px;
    letter-spacing: 2px;
    text-transform: uppercase;
  }
  /* Back */
  .card-back {
    top: 523px;
    background: linear-gradient(150deg, var(--cyan-pale) 0%, var(--cyan) 55%, var(--cyan-deep) 100%);
  }
  .back-wordmark {
    position: absolute;
    right: 64px;
    bottom: 70px;
    display: flex;
    align-items: center;
    gap: 16px;
  }
  .back-wordmark .brand-dot { background: var(--back-text); width: 40px; height: 40px; }
  .back-wordmark .brand-name { color: var(--back-text); font-size: 42px; }
</style>
</head>
<body>
  <section class="card card-front" aria-label="Business card front">
    <div class="brand-mark">
      <span class="brand-dot"></span>
      <span class="brand-name">Silverline<br>Dentistry</span>
    </div>

    <h1 class="doctor">Elliot Marsh, <span class="credentials">DDS, MMSc</span></h1>

    <ul class="contact-list">
      <li>
        <svg class="contact-icon" viewBox="0 0 20 20" aria-hidden="true"><rect width="20" height="20" rx="3" fill="#c9cfd2"/><path d="M6 4.5l2 2-1.2 1.6c.8 1.7 2 2.9 3.6 3.7l1.5-1.2 2 2-1.4 1.8C8.8 14 5.8 11 4.6 6.2z" fill="#0d0f10"/></svg>
        555-014-2286
      </li>
      <li>
        <svg class="contact-icon" viewBox="0 0 20 20" aria-hidden="true"><rect width="20" height="20" rx="3" fill="#c9cfd2"/><rect x="4" y="6" width="12" height="8" fill="none" stroke="#0d0f10" stroke-width="1.4"/><path d="M4 6l6 4.5L16 6" fill="none" stroke="#0d0f10" stroke-width="1.4"/></svg>
        elliot@silverlinedental.com
      </li>
      <li>
        <svg class="contact-icon" viewBox="0 0 20 20" aria-hidden="true"><rect width="20" height="20" rx="3" fill="#c9cfd2"/><circle cx="10" cy="10" r="5.5" fill="none" stroke="#0d0f10" stroke-width="1.3"/><path d="M4.5 10h11M10 4.5c-2.5 3-2.5 8 0 11M10 4.5c2.5 3 2.5 8 0 11" fill="none" stroke="#0d0f10" stroke-width="1.1"/></svg>
        www.silverlinedental.com
      </li>
    </ul>

    <span class="divider"></span>

    <address class="office">
      <div class="office-name">Silverline Dentistry</div>
      <div>214 alder row fairmont</div>
      <div>Westbrook, Colorado</div>
    </address>

    <div class="specialty-band">Smile Solutions | Prosthodontics | Implant Dentistry</div>
  </section>

  <section class="card card-back" aria-label="Business card back">
    <div class="back-wordmark">
      <span class="brand-dot"></span>
      <span class="brand-name">Silverline<br>Dentistry</span>
    </div>
  </section>
</body>
</html>
```